Easy Business Card / Presentation Cover Design Project

We are looking for a business card design, covers for powerpoint presentations for investors, and possibly simple stationary for a Chicago real estate development firm. Our new logo is attached below.

We rehab and provide newly constructed homes. We are not a real estate brokerage firm (i.e., agents such as Meridale 47) and only operate in the Chicago area.

In terms of design, sophisticated and high end that would appeal to investors (theme should resemble investment banks, hedge funds, private equity rather than tech startup).

Target Market(s)

Investors, banks, financing sources

Industry/Entity Type

Real Estate

Requirements
Must have
• Two deliverables here. 1) Business card 2) Covers for powerpoint presentation.

Must be able to look sophisticated and high end when printed. Please think through the type of printing that will be needed. Would prefer something that can be printed in raised ink but digital is ok as well.

Will be printed on heavy paper.

Business Card: Horizontal Layout, no black backgrounds,

For presentation front cover, should include logo only. For back cover, should include contact info. Horizontal and should not contain any information that will need to be changed (i.e. date or client name)
Nice to have
• Would like to have the edges colored but not required. Please show multiple designs
Should not have
• Should not have any die cut or embossed type of designs. Shape should be standard size.

We are not a design firm, a retail firm, or a consumer product firm.

Please do not incorporate a house, buildings, etc. This must be very professional looking.

```html
<!DOCTYPE html>
<html lang="en">
<head>
<meta charset="utf-8">
<title>Kestrel Realty – Business Card</title>
<link href="https://fonts.googleapis.com/css2?family=Jost:wght@400;500&display=swap" rel="stylesheet">
<style>
  :root {
    --stage: #3b3b3b;
    --card: #ffffff;
    --facet-1: #f1f1f1;
    --facet-2: #e9e9e9;
    --facet-3: #f6f6f6;
    --ink: #333333;
    --ink-soft: #4a4a4a;
    --accent: #2f8fe0;
    --rule: #3c3c3c;
  }
  * { margin: 0; padding: 0; box-sizing: border-box; }
  html, body {
    width: 1200px;
    height: 1000px;
    overflow: hidden;
    background: var(--stage);
    font-family: "Jost", "Futura", sans-serif;
  }
  .sheet {
    position: relative;
    width: 1200px;
    height: 1000px;
    display: flex;
    justify-content: center;
    align-items: center;
    gap: 40px;
  }
  .card {
    position: relative;
    width: 540px;
    height: 310px;
    background: var(--card);
    overflow: hidden;
    box-shadow: 0 10px 30px rgba(0,0,0,0.35);
  }
  .card__facets {
    position: absolute;
    inset: 0;
    width: 100%;
    height: 100%;
  }
  .brand {
    position: absolute;
    display: flex;
    align-items: center;
    color: var(--ink);
  }
  .brand__dot {
    border-radius: 50%;
    background: var(--accent);
    flex: none;
  }
  .brand__name {
    font-weight: 500;
    color: var(--ink);
    line-height: 0.95;
    letter-spacing: 0.02em;
  }
  /* front */
  .card--front .brand {
    left: 150px;
    top: 108px;
    gap: 18px;
  }
  .card--front .brand__dot { width: 86px; height: 86px; }
  .card--front .brand__name { font-size: 40px; }
  .card--front .brand__name span { display: block; font-size: 27px; }
  .front__rule {
    position: absolute;
    left: 140px;
    top: 222px;
    width: 270px;
    height: 2px;
    background: linear-gradient(90deg, rgba(60,60,60,0), var(--rule) 30%, var(--rule) 75%, rgba(60,60,60,0));
  }
  /* back */
  .card--back .brand {
    right: 34px;
    top: 30px;
    gap: 8px;
  }
  .card--back .brand__dot { width: 36px; height: 36px; }
  .card--back .brand__name { font-size: 17px; }
  .card--back .brand__name span { display: block; font-size: 12px; }
  .contact {
    position: absolute;
    left: 40px;
    top: 148px;
  }
  .contact__company {
    font-size: 22px;
    font-weight: 500;
    color: var(--ink);
    margin-bottom: 10px;
  }
  .contact__list { list-style: none; }
  .contact__item {
    display: flex;
    align-items: center;
    gap: 12px;
    font-size: 12.5px;
    color: var(--ink-soft);
    height: 24px;
  }
  .contact__icon { width: 18px; height: 18px; flex: none; fill: var(--ink); }
</style>
</head>
<body>
<main class="sheet">

  <section class="card card--front" aria-label="Business card front">
    <svg class="card__facets" viewBox="0 0 540 310" preserveAspectRatio="none" aria-hidden="true">
      <polygon points="0,0 150,0 60,185 0,140" fill="var(--facet-1)"/>
      <polygon points="60,185 150,0 260,0" fill="var(--facet-3)"/>
      <polygon points="0,140 60,185 0,310" fill="var(--facet-2)"/>
      <polygon points="60,185 0,310 160,310" fill="var(--facet-3)"/>
      <polygon points="380,0 540,0 540,90" fill="var(--facet-3)"/>
    </svg>
    <div class="brand">
      <div class="brand__dot"></div>
      <div class="brand__name">KESTREL<span>REALTY</span></div>
    </div>
    <div class="front__rule"></div>
  </section>

  <section class="card card--back" aria-label="Business card back">
    <svg class="card__facets" viewBox="0 0 540 310" preserveAspectRatio="none" aria-hidden="true">
      <polygon points="300,0 540,0 540,60" fill="var(--facet-3)"/>
      <polygon points="0,220 120,310 0,310" fill="var(--facet-1)"/>
      <polygon points="120,310 0,220 240,310" fill="var(--facet-3)"/>
    </svg>
    <div class="brand">
      <div class="brand__dot"></div>
      <div class="brand__name">KESTREL<span>REALTY</span></div>
    </div>
    <div class="contact">
      <h1 class="contact__company">Kestrel Realty LLC</h1>
      <ul class="contact__list">
        <li class="contact__item">
          <svg class="contact__icon" viewBox="0 0 18 18" aria-hidden="true"><path d="M2 6c0-2 3-3 7-3s7 1 7 3v1.5h-3.5V6h-7v1.5H2z"/><rect x="3" y="9" width="12" height="7" rx="1.5"/></svg>
          +1 555-014-2900 | Fax-555.014.3555
        </li>
        <li class="contact__item">
          <svg class="contact__icon" viewBox="0 0 18 18" aria-hidden="true"><rect x="1" y="3" width="5" height="14"/><rect x="7" y="8" width="4" height="9"/><rect x="12" y="5" width="5" height="12"/></svg>
          410 W Lumen Ave, Chicago, IL 60600-0100
        </li>
        <li class="contact__item">
          <svg class="contact__icon" viewBox="0 0 18 18" aria-hidden="true"><rect x="1" y="4" width="16" height="11"/><path d="M1.5 4.5 9 10.5l7.5-6" fill="none" stroke="#fff" stroke-width="1.3"/></svg>
          Your Mail Address
        </li>
        <li class="contact__item">
          <svg class="contact__icon" viewBox="0 0 18 18" aria-hidden="true"><circle cx="9" cy="9" r="8"/></svg>
          http://kestrelrealty.com/
        </li>
      </ul>
    </div>
  </section>

</main>
</body>
</html>
```